Plakat-Design für ein Filmplakat
Zielgruppe
I would like to create a cinematic poster for my movie.
Aufgabenstellung
Below in attachment all information about the film to help designers to create the the movie poster.

```html
<!DOCTYPE html>
<html lang="en">
<head>
<meta charset="utf-8">
<title>Soven – Film Poster</title>
<link rel="stylesheet" href="https://fonts.googleapis.com/css2?family=Cinzel:wght@400;700&family=Oswald:wght@400;500&display=swap">
<style>
  :root {
    --page: #f2f2f2;
    --ink: #ffffff;
    --sky: #dfe7ec;
    --night: #16161d;
    --sea-deep: #123a5c;
    --sea: #2d6d9a;
    --foam: #c9dbe8;
    --rock: #23232b;
    --scarf: #c9271c;
    --skin: #c98f77;
    --hair: #d7a65a;
  }
  * { margin: 0; padding: 0; box-sizing: border-box; }
  html, body { width: 1200px; height: 1200px; overflow: hidden; background: var(--page); }
  .poster {
    position: absolute; left: 228px; top: 75px; width: 744px; height: 1050px;
    overflow: hidden; color: var(--ink); font-family: "Cinzel", serif;
  }
  .key-art {
    position: absolute; inset: 0;
    background:
      radial-gradient(ellipse 200px 170px at 260px 330px, var(--skin) 0%, rgba(201,143,119,0) 100%),
      radial-gradient(ellipse 220px 130px at 200px 200px, var(--hair) 0%, rgba(215,166,90,0) 100%),
      radial-gradient(ellipse 120px 200px at 50px 420px, var(--scarf) 0%, rgba(201,39,28,0) 100%),
      radial-gradient(ellipse 360px 260px at 560px 360px, #6f9fc4 0%, rgba(111,159,196,0) 100%),
      radial-gradient(ellipse 230px 220px at 110px 650px, var(--rock) 0%, rgba(35,35,43,0) 100%),
      linear-gradient(90deg, var(--sky) 0%, var(--sky) 55%, var(--night) 68%, var(--night) 100%) top / 100% 200px no-repeat,
      linear-gradient(180deg, #9fb4c4 0%, var(--sea) 55%, var(--sea-deep) 75%, var(--sea) 88%, var(--foam) 100%);
  }
  .shade {
    position: absolute; inset: 0;
    background: linear-gradient(180deg, rgba(0,0,0,0) 55%, rgba(8,20,35,.35) 100%);
  }
  .billing {
    position: absolute; top: 42px; font-size: 15px; letter-spacing: .5px;
    text-shadow: 0 1px 2px rgba(0,0,0,.6);
  }
  .billing--left { left: 72px; color: #fff; }
  .billing--right { right: 72px; }
  .title {
    position: absolute; top: 612px; left: 0; width: 100%; text-align: center;
    font-size: 152px; font-weight: 400; line-height: 1; letter-spacing: 2px;
    text-shadow: 0 3px 6px rgba(0,0,0,.55);
  }
  .tagline {
    position: absolute; top: 770px; left: 0; width: 100%; text-align: center;
    font-size: 43px; letter-spacing: 1px; text-shadow: 0 2px 4px rgba(0,0,0,.5);
  }
  .quote {
    position: absolute; top: 828px; left: 0; width: 100%; text-align: center;
    font-size: 22px; text-shadow: 0 1px 3px rgba(0,0,0,.5);
  }
  .credits-top {
    position: absolute; top: 868px; left: 90px; right: 90px;
    display: flex; justify-content: space-between; text-align: center;
    font-size: 10.5px; line-height: 14px; text-shadow: 0 1px 2px rgba(0,0,0,.6);
  }
  .credit-block {
    position: absolute; top: 910px; left: 70px; right: 70px; text-align: center;
    font-family: "Oswald", sans-serif; font-size: 10.5px; line-height: 16px;
    text-transform: uppercase; text-shadow: 0 1px 2px rgba(0,0,0,.7);
  }
  .credit-block small { font-size: 5.5px; letter-spacing: .2px; }
  .partners {
    position: absolute; bottom: 14px; left: 22px; right: 22px;
    display: flex; justify-content: space-between; align-items: center;
    font-size: 8.5px; letter-spacing: .6px; text-shadow: 0 1px 2px rgba(0,0,0,.6);
  }
  .partner { display: flex; align-items: center; gap: 5px; }
  .partner svg { flex: none; }
</style>
</head>
<body>
  <main class="poster">
    <div class="key-art" role="img" aria-label="Photograph of a grieving couple leaning together, a woman in a red scarf resting her head, above a dark sea cliff and stormy ocean waves"></div>
    <div class="shade"></div>

    <p class="billing billing--left">LEVAN MOTSARA</p>
    <p class="billing billing--right">TAMAR VELISHVARI</p>

    <h1 class="title">SOVEN</h1>
    <p class="tagline">INSPIRED BY A TRUE STORY</p>
    <p class="quote">“SOVEN” A MUST SEE MOVIE</p>

    <div class="credits-top">
      <p>DIRECTED BY<br>DARAN KHELVANY</p>
      <p>SCREENPLAY BY<br>DARAN KHELVANY &nbsp;ILO MARSENOVI</p>
      <p>STORY BY<br>DARAN KHELVANY</p>
    </div>

    <div class="credit-block">
      <p>Daran Khelvany <small>presents</small></p>
      <p><small>a</small> Khelvan Films <small>and</small> Atlas Bay Cinema <small>with logistical support of</small> RV Studio <small>and</small> Sahelprod <small>starring</small> Levan Motsara <small>and</small> Tamar Velishvari</p>
      <p>“Soven” <small>music by</small> Karim Ilyasi <small>costume designer</small> Ketino Berulavi <small>edited by</small> Daran Khelvany <small>production designer</small> Ketino Berulavi</p>
      <p><small>director of photography</small> Daran Khelvany <small>production manager-georgia unit</small> Zurab Meltavishvili <small>production manager-iraq unit</small> Rebaz Khelvany</p>
      <p><small>executive producer</small> Eka Dolidari <small>produced by</small> Daran Khelvany <small>screenplay by</small> Daran Khelvany <small>and</small> Ilo Marsenovi <small>directed by</small> Daran Khelvany</p>
    </div>

    <div class="partners">
      <span class="partner"><svg width="12" height="12"><circle cx="6" cy="6" r="5" fill="#fff"/></svg>KHELVAN FILMS</span>
      <span class="partner"><svg width="12" height="12"><rect x="1" y="1" width="10" height="10" fill="#fff"/></svg>ATLAS BAY CINEMA</span>
      <span class="partner"><svg width="12" height="12"><circle cx="6" cy="6" r="5" fill="#fff"/></svg>RV STUDIO</span>
      <span class="partner">FOUR TIDE MEDIA</span>
      <span class="partner"><svg width="12" height="12"><rect x="1" y="1" width="10" height="10" fill="#fff"/></svg>SURROUND 5.1</span>
      <span class="partner">CUTLINE EDITOR</span>
    </div>
  </main>
</body>
</html>
```